Need a new letterhead

Need a new fresh exciting letterhead. Remove the footer...info is outdated.

Target Market(s)

B2B

Industry/Entity Type

Electrical Power

Colors

Designer to choose colors to be used in the design.

Requirements
Must have
• Red and Blue Corvane Systems Logo
Nice to have
• Lighting the way to sustainability in footer...reorganize the words?

```html
<!DOCTYPE html>
<html lang="en">
<head>
<meta charset="utf-8">
<title>Corvane Systems Letterhead</title>
<link rel="stylesheet" href="https://fonts.googleapis.com/css2?family=Source+Sans+3:wght@400;600;800&display=swap">
<style>
  :root {
    --ink-black: #1b1b1b;
    --brand-red: #e8232a;
    --stripe-red: #b8372f;
    --stripe-dark: #7a2e28;
    --accent-blue: #6a72b4;
    --navy: #26358a;
    --text-grey: #666666;
    --paper: #ffffff;
  }
  * { margin: 0; padding: 0; box-sizing: border-box; }
  html, body { width: 848px; height: 1200px; overflow: hidden; background: var(--paper); }
  body { font-family: "Source Sans 3", sans-serif; color: var(--text-grey); }
  .letterhead { position: relative; width: 848px; height: 1200px; overflow: hidden; }

  .header-band { position: absolute; top: 0; left: 0; width: 848px; height: 152px; }
  .brand-name {
    position: absolute; top: 24px; right: 40px; width: 230px;
    font-weight: 800; font-size: 34px; line-height: 36px; letter-spacing: 1px;
    color: var(--brand-red); text-align: center; text-transform: uppercase;
  }

  .letter-body { position: absolute; left: 74px; top: 309px; width: 700px; font-size: 11.4px; line-height: 15.4px; }
  .meta-line { font-size: 12.8px; line-height: 21px; }
  .recipient { margin-top: 18px; }
  .recipient .salutation { font-size: 12.8px; line-height: 17px; }
  .recipient p { font-size: 11.6px; line-height: 15.6px; }
  .subject { margin-top: 15px; font-size: 11.6px; }
  .body-text p { margin-top: 15px; text-align: justify; }

  .sign-off { position: absolute; left: 74px; top: 736px; }
  .sign-off .signer { font-size: 10.2px; }
  .sign-off .role { font-size: 13px; margin-top: 2px; }

  .footer-band { position: absolute; left: 0; top: 1076px; width: 848px; height: 16px; }
  .footer-brand {
    position: absolute; left: 28px; top: 1102px; width: 220px;
    font-weight: 800; font-size: 32px; line-height: 34px; letter-spacing: 1px;
    color: var(--brand-red); text-align: center; text-transform: uppercase;
  }
  .contact-list { position: absolute; left: 350px; top: 1114px; width: 460px; height: 46px; display: flex; list-style: none; }
  .contact-item { display: flex; flex-direction: column; align-items: center; font-size: 8px; line-height: 11px; text-align: center; color: #777; }
  .contact-item svg { width: 12px; height: 12px; margin: 2px 0 4px; }
  .contact-item + .contact-item { border-left: 1px solid #cfcfcf; }
  .contact-item:nth-child(1) { width: 116px; }
  .contact-item:nth-child(2) { width: 109px; }
  .contact-item:nth-child(3) { width: 112px; }
  .contact-item:nth-child(4) { width: 123px; }
</style>
</head>
<body>
<div class="letterhead">

  <svg class="header-band" viewBox="0 0 848 152" aria-hidden="true">
    <polygon points="0,0 848,0 848,152 520,152 489,120 0,120" fill="var(--accent-blue)"/>
    <polygon points="0,0 848,0 848,143 520,143 489,111 0,111" fill="var(--ink-black)"/>
    <defs>
      <radialGradient id="redGlow" cx="0.5" cy="0.5" r="0.7">
        <stop offset="0" stop-color="#f4473b"/>
        <stop offset="1" stop-color="var(--brand-red)"/>
      </radialGradient>
    </defs>
    <polygon points="0,0 95,0 172,111 0,111" fill="url(#redGlow)"/>
    <polygon points="118,0 140,0 217,111 195,111" fill="var(--stripe-red)"/>
    <polygon points="163,0 185,0 262,111 240,111" fill="#9e3630"/>
    <polygon points="207,0 229,0 306,111 284,111" fill="#7f302a"/>
    <polygon points="251,0 268,0 345,111 328,111" fill="#5a2b27"/>
  </svg>
  <div class="brand-name">Corvane<br>Systems</div>

  <main class="letter-body">
    <p class="meta-line">REF: 12EC1428</p>
    <p class="meta-line">DATE: 12 DEC 2014</p>

    <div class="recipient">
      <p class="salutation">TO</p>
      <p>MR. DANIEL MARLOW</p>
      <p>Director, Northfield Medical Limited</p>
      <p>48/6, Riverside Lane, Dhaka-1205, BD</p>
    </div>

    <p class="subject">Proposal for work with us as a communication partner</p>

    <div class="body-text">
      <p>Lorem ipsum dolor sit amet, consectetuer adipiscing elit, sed diam nonummy nibh euismod tincidunt ut laoreet dolore magna aliquam erat volutpat. Ut wisi enim ad minim veniam, quis nostrud exerci tation ullamcorper suscipit lobortis nisl ut aliquip ex ea commodo consequat. Duis autem vel eum iriure dolor in hendrerit in vulputate velit esse molestie consequat vel illum dolore eu feugiat nulla facilisis at vero eros et accumsan et iusto odio dignissim qui blandit praesent luptatum zzril delenit augue duis dolore te feugait nulla facilisi. Nam liber tempor cum soluta nobis eleifend option congue nihil imperdiet doming id quod mazim placerat facer possim assum. Typi non habent claritatem insitam; est usus legentis in iis qui facit eorum claritatem. Investigationes demonstraverunt lectores legere me lius quod ii l</p>
      <p>egunt saepius. Claritas est etiam processus dynamicus, qui sequitur mutationem consuetudium lectorum. Mirum est notare quam littera gothica, quam nunc putamus parum claram, anteposuerit litterarum formas humanitatis per seacula quarta decima et quinta decima. Eodem modo typi, qui nunc nobis videntur parum clari, fiant sollemnes in futurum.</p>
    </div>
  </main>

  <div class="sign-off">
    <p class="signer">Mr. Tarek Hossain</p>
    <p class="role">Account Manager</p>
  </div>

  <svg class="footer-band" viewBox="0 0 848 16" aria-hidden="true">
    <polygon points="0,2 331,2 344,14 848,14 848,2 848,0 0,0" fill="var(--navy)"/>
    <rect x="0" y="0" width="848" height="3" fill="var(--navy)"/>
    <polygon points="330,0 848,0 848,14 344,14" fill="var(--navy)"/>
  </svg>
  <div class="footer-brand">Corvane<br>Systems</div>

  <ul class="contact-list">
    <li class="contact-item">
      <svg viewBox="0 0 12 12"><path d="M6 0.5a4 4 0 0 0-4 4c0 3 4 7 4 7s4-4 4-7a4 4 0 0 0-4-4z" fill="#222"/><circle cx="6" cy="4.5" r="1.5" fill="#fff"/></svg>
      <span>123, your address here</span><span>Dhaka, 1205, BD</span>
    </li>
    <li class="contact-item">
      <svg viewBox="0 0 12 12"><rect x="0.7" y="2.5" width="10.6" height="7" fill="none" stroke="#222" stroke-width="0.9"/><path d="M0.7 2.5L6 7l5.3-4.5M0.7 9.5L4.5 6M11.3 9.5L7.5 6" fill="none" stroke="#222" stroke-width="0.9"/></svg>
      <span>yourmail@url.com</span><span>mail@url.com</span>
    </li>
    <li class="contact-item">
      <svg viewBox="0 0 12 12"><circle cx="6" cy="6" r="5.2" fill="none" stroke="#222" stroke-width="1.2"/><path d="M0.8 6h10.4M6 0.8c-2.5 3-2.5 7.4 0 10.4M6 0.8c2.5 3 2.5 7.4 0 10.4" fill="none" stroke="#222" stroke-width="1"/></svg>
      <span>www.yoursite.com</span><span>www.siteurl.com</span>
    </li>
    <li class="contact-item">
      <svg viewBox="0 0 12 12"><circle cx="6" cy="6" r="5.2" fill="none" stroke="#222" stroke-width="1.2"/><path d="M4 3.2l1.2 1.6-0.7 0.8c0.5 1 1.1 1.6 2 2l0.8-0.7 1.5 1.2-0.8 1c-2.4-0.4-4.3-2.4-4.8-4.9z" fill="#222"/></svg>
      <span>+111 222 333</span><span>(9 am- 10 pm) UST</span>
    </li>
  </ul>

</div>
</body>
</html>
```